Custom Business Card Design

We are looking for a raised spot logo design to use with Plinkory.com. We will provide the logo files. Should be a front and back design. We want to implement the house into the back design using the same colors as the logo through out. Something VERY cool!

Industry/Entity Type

Business

```html
<!DOCTYPE html>
<html lang="en">
<head>
<meta charset="utf-8">
<title>Plinkory business card – front and back</title>
<link href="https://fonts.googleapis.com/css2?family=Roboto:wght@400;500;700&display=swap" rel="stylesheet">
<style>
  :root {
    --bg: #e9e4dc;
    --card-white: #f7f7f7;
    --brand-blue: #2f74b0;
    --brand-red: #e2414b;
    --ink-grey: #6d6d6d;
    --ink-dark: #4a4a4a;
    --white: #ffffff;
  }
  * { margin: 0; padding: 0; box-sizing: border-box; }
  html, body { width: 1200px; height: 1023px; overflow: hidden; }
  body {
    background: var(--bg);
    font-family: "Roboto", Arial, sans-serif;
    position: relative;
  }
  .card {
    position: absolute;
    left: 270px;
    width: 660px;
    height: 377px;
    border-radius: 4px;
    box-shadow: 0 10px 28px rgba(60, 45, 25, 0.25);
    overflow: hidden;
  }
  .card--front { top: 90px; background: var(--card-white); }
  .card--back { top: 556px; background: var(--brand-blue); }

  /* front */
  .wordmark {
    position: absolute;
    display: flex;
    align-items: center;
    gap: 12px;
  }
  .wordmark__rule {
    position: absolute;
    left: 0; right: 0;
    height: 2px;
  }
  .wordmark__rule--top { top: -10px; }
  .wordmark__rule--bottom { bottom: -10px; }
  .wordmark__dot { border-radius: 50%; flex: none; }
  .wordmark__name { font-weight: 700; letter-spacing: 0.5px; line-height: 1; }

  .card--front .wordmark { left: 46px; top: 92px; }
  .card--front .wordmark__rule { background: var(--brand-blue); }
  .card--front .wordmark__dot { width: 40px; height: 40px; background: var(--brand-blue); }
  .card--front .wordmark__name { font-size: 48px; color: var(--brand-blue); }

  .person { position: absolute; left: 50px; top: 202px; }
  .person__name { font-size: 22px; font-weight: 500; color: var(--brand-blue); }
  .person__role { font-size: 17px; color: var(--brand-red); margin-top: 2px; }

  .divider { position: absolute; top: 214px; left: 208px; right: 40px; height: 2px; display: flex; }
  .divider__dotted { width: 130px; border-top: 2px dotted var(--brand-blue); }
  .divider__solid { flex: 1; background: var(--brand-red); height: 1.5px; }

  .contacts { position: absolute; left: 50px; top: 268px; list-style: none; }
  .contacts li {
    display: flex; align-items: center; gap: 9px;
    font-size: 15px; color: var(--ink-dark); height: 22px;
  }
  .contacts svg { width: 15px; height: 15px; flex: none; }
  .contacts .accent { color: var(--brand-red); }

  .address {
    position: absolute; right: 40px; bottom: 42px;
    text-align: right; font-size: 15px; line-height: 1.35; color: var(--ink-grey);
  }

  /* back */
  .card--back .wordmark { left: 50%; top: 50%; transform: translate(-50%, -50%); gap: 18px; }
  .card--back .wordmark__rule { background: var(--white); }
  .card--back .wordmark__rule--top { top: -14px; }
  .card--back .wordmark__rule--bottom { bottom: -14px; }
  .card--back .wordmark__dot { width: 76px; height: 76px; background: var(--white); }
  .card--back .wordmark__name { font-size: 66px; color: var(--white); }
</style>
</head>
<body>

<section class="card card--front" aria-label="Card front">
  <div class="wordmark">
    <span class="wordmark__rule wordmark__rule--top"></span>
    <span class="wordmark__dot"></span>
    <span class="wordmark__name">Plinkory</span>
    <span class="wordmark__rule wordmark__rule--bottom"></span>
  </div>

  <div class="person">
    <p class="person__name">Dana Whitlow</p>
    <p class="person__role">Founder</p>
  </div>

  <div class="divider">
    <span class="divider__dotted"></span>
    <span class="divider__solid"></span>
  </div>

  <ul class="contacts">
    <li>
      <svg viewBox="0 0 16 16"><circle cx="8" cy="8" r="8" fill="#2f74b0"/><path d="M5.5 4.5l1.6-.3.8 2-1 .8a5 5 0 0 0 2.1 2.1l.8-1 2 .8-.3 1.6c-3.5.2-6.2-2.5-6-6z" fill="#fff"/></svg>
      +555 01 2340
    </li>
    <li>
      <svg viewBox="0 0 16 16"><circle cx="8" cy="8" r="8" fill="#2f74b0"/><rect x="4.5" y="5" width="7" height="6" rx="0.8" fill="#fff"/><rect x="5.8" y="3.6" width="4.4" height="2" fill="#fff"/></svg>
      +555 01 7789
    </li>
    <li>
      <svg viewBox="0 0 16 16"><circle cx="8" cy="8" r="8" fill="#2f74b0"/><rect x="4" y="5" width="8" height="6" fill="#fff"/><path d="M4 5l4 3.2L12 5" stroke="#2f74b0" stroke-width="1" fill="none"/></svg>
      info@plinkory.com
    </li>
    <li>
      <svg viewBox="0 0 16 16"><circle cx="8" cy="8" r="8" fill="#2f74b0"/><circle cx="8" cy="8" r="4.2" fill="none" stroke="#fff" stroke-width="1"/><path d="M3.8 8h8.4M8 3.8c-2 2.5-2 5.9 0 8.4M8 3.8c2 2.5 2 5.9 0 8.4" stroke="#fff" stroke-width="0.8" fill="none"/></svg>
      <span>www.<span class="accent">plinkory</span>.com</span>
    </li>
  </ul>

  <p class="address">Here your company or<br>home address</p>
</section>

<section class="card card--back" aria-label="Card back">
  <div class="wordmark">
    <span class="wordmark__rule wordmark__rule--top"></span>
    <span class="wordmark__dot"></span>
    <span class="wordmark__name">Plinkory</span>
    <span class="wordmark__rule wordmark__rule--bottom"></span>
  </div>
</section>

</body>
</html>
```